Flyer for Institute Party

This event has changed to the following - March 24th, 2017 from 4-6pm in the Halvern Medical Education Center Atrium (You can get to the Atrium from the Brenwick elevators by getting off on the 5th floor or from the Larkfield Pavilion elevators by getting off on the 5th floor). I have attached the logo of the Institute as well to add to the flyer. Also, the Morvane Institute just became and Institute in January 2017, so it would be nice to note that as part of the celebration in the flyer someplace. We have a lot to celebrate! I am looking for a fun flyer to for an Institute party. We would like to celebrate becoming an Institute and the labs within the Institute at the party.

```html
<!DOCTYPE html>
<html lang="en">
<head>
<meta charset="utf-8">
<title>International Day of Awesomeness – Morvane Institute</title>
<link rel="stylesheet" href="https://fonts.googleapis.com/css2?family=Pacifico&family=Oswald:wght@400;500&family=Courier+Prime&display=swap">
<style>
  :root {
    --stage: #d6d6d6;
    --paper: #ffffff;
    --sky-top: #8fc3e6;
    --sky-bottom: #a9d2ec;
    --red: #b0202a;
    --blue: #1c7fd0;
    --navy: #1f2f6b;
    --grey-text: #555555;
    --dots: #777777;
  }
  * { box-sizing: border-box; margin: 0; padding: 0; }
  html, body { width: 1200px; height: 837px; overflow: hidden; background: var(--stage); }
  .flyer {
    position: absolute; left: 40px; top: 57px;
    width: 1120px; height: 723px;
    background: var(--paper); overflow: hidden;
  }
  .hero {
    position: absolute; left: 0; top: 0; width: 100%; height: 428px;
    background:
      radial-gradient(circle at 25% 30%, rgba(240,170,150,.45), transparent 30%),
      radial-gradient(circle at 75% 40%, rgba(160,200,120,.4), transparent 30%),
      radial-gradient(circle at 50% 80%, rgba(230,120,130,.35), transparent 35%),
      linear-gradient(180deg, var(--sky-top), var(--sky-bottom));
  }
  .hero-title {
    position: absolute; left: 0; width: 100%; top: 110px;
    text-align: center; color: var(--paper);
    font-family: "Pacifico", cursive; font-size: 64px; line-height: 1; font-weight: 400;
  }
  .ribbon { position: absolute; left: 129px; top: 188px; width: 908px; height: 126px; }
  .ribbon svg { position: absolute; inset: 0; }
  .ribbon-label {
    position: absolute; left: 68px; right: 68px; top: 0; height: 126px;
    display: flex; align-items: center; justify-content: center;
    font-family: "Oswald", sans-serif; font-weight: 500; font-size: 38px;
    color: var(--red); letter-spacing: .5px;
  }
  .by-badge {
    position: absolute; left: 523px; top: 352px; width: 62px; height: 62px;
    border-radius: 50%; background: var(--red); color: var(--paper);
    display: flex; align-items: center; justify-content: center;
    font-family: "Pacifico", cursive; font-size: 26px; line-height: 1;
  }
  .tagline {
    position: absolute; left: 0; width: 100%; top: 435px; text-align: center;
    font-family: "Oswald", sans-serif; font-weight: 500; font-size: 23px;
    color: var(--blue); letter-spacing: .3px;
  }
  .rule { position: absolute; left: 50px; right: 50px; top: 474px; border-top: 2px dotted var(--dots); }
  .divider { position: absolute; top: 490px; height: 170px; border-left: 2px dotted var(--dots); }
  .divider.first { left: 404px; }
  .divider.second { left: 697px; }
  .presenter { position: absolute; left: 55px; top: 490px; width: 330px; }
  .presenter-label { font-family: "Courier Prime", monospace; font-size: 15px; color: #333; }
  .presenter-name {
    margin-top: 46px; display: flex; align-items: center; gap: 14px;
    font-family: "Oswald", sans-serif; font-weight: 500; font-size: 40px; color: var(--navy);
  }
  .presenter-name .dot { width: 42px; height: 42px; border-radius: 50%; background: var(--navy); flex: none; }
  .fact-seal {
    position: absolute; left: 480px; top: 505px; width: 148px; height: 148px;
    border-radius: 50%; border: 3px dotted var(--navy);
    display: flex; flex-direction: column; align-items: center; justify-content: center; text-align: center;
  }
  .fact-top, .fact-bottom { font-family: "Oswald", sans-serif; font-weight: 500; font-size: 20px; }
  .fact-top { color: var(--red); border-bottom: 1px solid var(--red); padding: 0 6px; }
  .fact-bottom { color: var(--navy); border-top: 1px solid var(--navy); padding: 0 14px; margin-top: 6px; }
  .fact-text { font-family: "Courier Prime", monospace; font-size: 11.5px; color: var(--red); line-height: 1.2; margin-top: 6px; width: 110px; }
  .event { position: absolute; left: 716px; top: 488px; width: 380px; }
  .event-when { position: absolute; left: 0; top: 0; width: 192px; color: var(--blue); font-family: "Oswald", sans-serif; font-weight: 500; }
  .event-date { font-size: 18px; line-height: 1.2; white-space: nowrap; }
  .event-time { font-size: 66px; line-height: 1; margin-top: 6px; white-space: nowrap; }
  .event-time small { font-size: 17px; vertical-align: 28px; margin: 0 2px; }
  .event-time .pm { font-size: 28px; vertical-align: 0; }
  .event-where {
    position: absolute; left: 196px; top: 2px; width: 184px;
    border-left: 3px solid var(--red); padding-left: 8px;
    display: flex; gap: 6px; align-items: flex-start;
  }
  .event-where .mark { width: 12px; height: 12px; background: var(--red); flex: none; margin-top: 6px; }
  .event-venue { font-family: "Oswald", sans-serif; font-weight: 500; font-size: 19px; line-height: 1.1; color: var(--blue); }
  .event-directions {
    position: absolute; left: 0; top: 106px; width: 370px;
    font-family: "Courier Prime", monospace; font-size: 13px; line-height: 1.3; color: var(--grey-text);
  }
</style>
</head>
<body>
<main class="flyer">
  <div class="hero" role="img" aria-label="Photograph of many colourful balloons floating up into a blue sky"></div>
  <h1 class="hero-title">Celebrate!</h1>
  <div class="ribbon">
    <svg viewBox="0 0 908 126" width="908" height="126" aria-hidden="true">
      <polygon points="0,22 78,22 78,98 0,98 22,60" fill="var(--red)"/>
      <polygon points="908,22 830,22 830,98 908,98 886,60" fill="var(--red)"/>
      <rect x="68" y="0" width="772" height="126" fill="#fff"/>
      <rect x="76" y="8" width="756" height="110" fill="none" stroke="var(--red)" stroke-width="3"/>
      <line x1="90" y1="22" x2="818" y2="22" stroke="var(--red)" stroke-width="2.5" stroke-dasharray="1 6" stroke-linecap="round"/>
      <line x1="90" y1="104" x2="818" y2="104" stroke="var(--red)" stroke-width="2.5" stroke-dasharray="1 6" stroke-linecap="round"/>
    </svg>
    <div class="ribbon-label">THE INTERNATIONAL DAY OF AWESOMENESS</div>
  </div>
  <div class="by-badge">By</div>

  <p class="tagline">CELEBRATING AWESOMENESS IN THE LABS OF THE MORVANE INSTITUTE</p>
  <div class="rule"></div>
  <div class="divider first"></div>
  <div class="divider second"></div>

  <section class="presenter">
    <p class="presenter-label">Proudly Brought to you by:</p>
    <p class="presenter-name"><span class="dot"></span>Morvane Institute</p>
  </section>

  <section class="fact-seal">
    <span class="fact-top">AWESOME</span>
    <span class="fact-text">WE BECAME AN INSTITUTE IN JANUARY 2017!</span>
    <span class="fact-bottom">FACT</span>
  </section>

  <section class="event">
    <div class="event-when">
      <p class="event-date">MARCH 24TH, 2017 FROM</p>
      <p class="event-time">4<small>TO</small>6<span class="pm"> PM</span></p>
    </div>
    <div class="event-where">
      <span class="mark"></span>
      <p class="event-venue">THE HALVERN MEDICAL EDUCATION CENTER ATRIUM</p>
    </div>
    <p class="event-directions">You can get to the Atrium from the Brenwick elevators by getting off on the 5th floor or from the Larkfield Pavilion elevators by getting off on the 5th floor.</p>
  </section>
</main>
</body>
</html>
```